Design a few pages of a luxury magazine for the Prestige Aubergerie Lyon

We need a luxury design for our magazine. See the inDesign pages of the current version attached (zip).

Please work primarily on the first double page (Inventez le luxe de demain) that contains only one photo with legend, a title and the text both in French and English. It must be made clear that the text is the same in two different languages (it is not clear enough here).

You can also work on the other two double pages selected. Feedback will be provided and the 10 best pages will be submitted to a vote at the end of the project timespan.

The most important is a classy and luxury design, this will be printed on expensive paper.

See the full brochure here: https://www.prestigeaubergerie.com/brochure/#page=4

Target Market(s)

Students and parents

Industry/Entity Type

Education

Colors

Designer to choose colors to be used in the design.

Requirements
Must have
• Luxury magazine layout, see:
• https://www.findwerk.com/search?q=luxury+magazine+layout&client=safari&rls=en&source=lnms&tbm=isch&sa=X&ved=0ahUKEwitoIDmit7fAhUVShUIHXC2Cd4Q_AUIDigB&biw=1010&bih=702
Nice to have
• The color of the cover that should be used for blue and grey is #393d49.
• Our font for serif titles (from the logo) is Adobe TRAJAN.
Should not have
• flashy colors

```html
<!DOCTYPE html>
<html lang="fr">
<head>
<meta charset="utf-8">
<title>Inventez le luxe de demain — Prestige Aubergerie Lyon</title>
<link rel="stylesheet" href="https://fonts.googleapis.com/css2?family=Fira+Sans:ital,wght@0,300;0,400;0,500;0,600;0,700;1,400&display=swap">
<style>
  :root {
    --slate: #393d49;
    --sand: #e3c797;
    --gold: #dfc08a;
    --amber: #e3993a;
    --mist: #b9b9bb;
    --ink: #2c2f3a;
    --white: #ffffff;
  }
  * { box-sizing: border-box; margin: 0; padding: 0; }
  html, body { width: 1200px; height: 764px; overflow: hidden; background: var(--sand); }
  body { font-family: "Fira Sans", sans-serif; position: relative; }
  .spread { position: relative; width: 1200px; height: 764px; background: var(--sand); overflow: hidden; }

  .page-left-panel { position: absolute; left: 0; top: 0; width: 333px; height: 764px; background: var(--slate); }

  .header-band { position: absolute; left: 0; top: 40px; width: 1200px; height: 40px; }
  .header-fr {
    position: absolute; left: 52px; top: 53px;
    color: var(--white); font-weight: 300; font-size: 12.5px; letter-spacing: 2.4px;
  }
  .header-en {
    position: absolute; right: 50px; top: 50px;
    color: var(--white); font-weight: 600; font-size: 18.5px; letter-spacing: 0.1px;
  }

  .fold-line { position: absolute; left: 599px; top: 0; height: 764px; border-left: 1px dashed #8f8a80; opacity: .7; }

  .title { position: absolute; left: 47px; top: 112px; width: 264px; line-height: 1; }
  .title-top { display: block; color: var(--white); font-weight: 700; font-size: 53px; letter-spacing: -0.6px; }
  .title-main { display: block; color: var(--gold); font-weight: 700; font-size: 117px; letter-spacing: -2px; margin-top: -8px; margin-left: -3px; }
  .title-bottom { display: block; color: var(--white); font-weight: 400; font-size: 50px; letter-spacing: 0.6px; margin-top: -8px; }

  .lang-tag {
    position: absolute; display: flex; align-items: center; gap: 7px;
    font-size: 8px; font-weight: 500; letter-spacing: 2px; text-transform: uppercase;
  }
  .lang-tag::before { content: ""; width: 14px; height: 1px; background: currentColor; }
  .lang-tag-fr { left: 50px; top: 338px; color: var(--gold); }
  .lang-tag-en { left: 1002px; top: 98px; width: 150px; justify-content: center; color: var(--amber); }
  .lang-tag-en::after { content: ""; width: 14px; height: 1px; background: currentColor; }

  .body-fr {
    position: absolute; left: 50px; top: 359px; width: 260px;
    color: var(--white); font-size: 9.8px; line-height: 16.4px; text-align: justify; font-weight: 300;
  }
  .body-fr p + p { margin-top: 14px; }

  .photo {
    position: absolute; left: 334px; top: 117px; width: 650px; height: 521px;
    background:
      radial-gradient(ellipse at 50% 30%, rgba(255,226,160,.55), transparent 55%),
      radial-gradient(ellipse at 50% 85%, #cdb896 0%, transparent 60%),
      linear-gradient(180deg, #3f3d33 0%, #6b5f44 40%, #8a7c5d 70%, #b6a581 100%);
  }

  .caption {
    position: absolute; left: 340px; top: 658px; width: 640px;
    color: var(--ink); font-size: 10px; line-height: 17.5px; text-align: center; font-style: italic;
  }
  .caption .name { font-style: normal; font-weight: 500; text-transform: uppercase; }
  .caption .role { font-style: normal; font-weight: 400; }

  .body-en {
    position: absolute; left: 1000px; top: 116px; width: 154px;
    color: var(--ink); font-size: 10px; line-height: 15.4px; text-align: center; font-weight: 300;
  }
  .body-en p + p { margin-top: 14px; }

  .folio { position: absolute; top: 726px; width: 18px; height: 18px; }
  .folio-left { left: 41px; }
  .folio-right { left: 1141px; }
  .folio-num { position: absolute; top: 730px; width: 18px; text-align: center; font-size: 8px; color: var(--white); }
</style>
</head>
<body>
<main class="spread">
  <div class="page-left-panel"></div>

  <svg class="header-band" width="1200" height="40" viewBox="0 0 1200 40" aria-hidden="true">
    <polygon points="262,0 677,0 692,40 280,40" fill="var(--mist)"/>
    <polygon points="0,0 262,0 280,40 0,40" fill="var(--amber)"/>
    <polygon points="660,0 1200,0 1200,40 677,40" fill="var(--amber)"/>
  </svg>
  <div class="header-fr">À LA PRESTIGE AUBERGERIE</div>
  <div class="header-en">Invent tomorrow’s luxuries at the Prestige Aubergerie</div>

  <h1 class="title">
    <span class="title-top">inventez le</span>
    <span class="title-main">LUXE</span>
    <span class="title-bottom">DE DEMAIN</span>
  </h1>

  <div class="lang-tag lang-tag-fr">Français</div>
  <div class="body-fr" lang="fr">
    <p>Depuis sa création il y a 30 ans, notre école garde le même objectif : que chaque étudiant acquière les compétences et développe les talents essentiels pour briller dans l’univers du luxe. Première école dédiée à l’hôtellerie de luxe, la Prestige Aubergerie délivre un Bachelor et un Master of Science in International Tourism and Hospitality Management, deux grades universitaires anglais.</p>
    <p>Cette combinaison du luxe à la française et du management anglosaxon donne toutes les clés à nos étudiants pour s’assurer une place privilégiée dans l’univers du luxe en France et à l’international.</p>
    <p>Grâce à l’excellence académique de nos programmes, la dimension internationale de nos formations et l’immersion professionnelle à travers des stages dans les plus prestigieux hôtels du monde, tous nos diplômés sont assurés de faire carrière dans le secteur de leur choix à un poste stratégique. La moitié d’entre eux signent un CDI avant même la fin de leur dernier stage.</p>
  </div>

  <div class="photo" role="img" aria-label="Photo de l’équipe de direction, quatre personnes posant dans un salon d’hôtel de luxe éclairé de lustres"></div>

  <p class="caption">
    De gauche à droite, l’équipe de Direction de la Prestige Aubergerie dans les salons du Palais Verano :
    <span class="name">Jean-Marc Delorme</span> <span class="role">- Vice-Président,</span><br>
    <span class="name">Amara Leclerc</span> <span class="role">- Directeur des opérations,</span>
    <span class="name">Sofia Garnier</span> <span class="role">- Responsable pédagogique,</span>
    <span class="name">Antoine Bellamy</span> <span class="role">- Président</span>
  </p>

  <div class="lang-tag lang-tag-en">English</div>
  <div class="body-en" lang="en">
    <p>Since its foundation 30 years ago, our school has had only one objective: that each student acquires the skills and develops the essential talents they require to shine within the luxury sector. The we offer a Bachelor’s and a Master’s degree in International Tourism and Hospitality Management.</p>
    <p>This combination of French-style luxury and Anglo-Saxon management gives our students the key elements they need to ensure a privileged position within the luxury industry both in France and internationally.</p>
    <p>The academic excellence of our programmes, the international dimension of our training and our professional work placements at the most prestigious hotels in the world all ensure that our graduates are certain to secure a career in a strategic role in the luxury sector. Half of Prestige Aubergerie is the first Higher Education establishment dedicated to luxury hotel training: our students sign a permanent contract before they even finish their final work placement.</p>
  </div>

  <div class="fold-line"></div>

  <svg class="folio folio-left" viewBox="0 0 18 18" aria-hidden="true"><polygon points="9,0 18,9 9,18 0,9" fill="var(--amber)" opacity=".85"/></svg>
  <span class="folio-num" style="left:41px">4</span>
  <svg class="folio folio-right" viewBox="0 0 18 18" aria-hidden="true"><polygon points="9,0 18,9 9,18 0,9" fill="var(--slate)"/></svg>
  <span class="folio-num" style="left:1141px">5</span>
</main>
</body>
</html>
```